Solo Law Practice Website Design

I am starting a solo law practice that will specialize in criminal defense and family law.

I have a rudimentary understanding of Wordpress as used through the tidalnest web services. The winning design would be compatible with this system so that I can modify content on my own.

I have supplied the written content and the components that I am looking for at the domain name: morganvaleslaw.com.

I would like to take that content and work it into a website that looks more professional and inviting. The two most important goals of the website are ease of navigation and rich content for search engine spiders (for example, integrating articles into pages rather than linking to a word document).

The winning design should be turnkey for me to upload immediately.
Updates

Reason: I will be traveling.

Target Market(s)

Individuals looking for legal services.

Industry/Entity Type

Defense

Requirements
Must have
• My picture should appear at least once in the site.

The design should allow a space for me to post blog or legal updates. Additionally, there should be functionality for me to add additional articles to the site.
Nice to have
• Appropriate pictures for a legal website to break-up text on pages.

Simple flash features that won't significantly slow loading times.

Widgets that drive traffic to a contact page or function.

```html
<!DOCTYPE html>
<html lang="en">
<head>
<meta charset="utf-8">
<title>Law Offices of Morgan Vales, PLLC</title>
<link href="https://fonts.googleapis.com/css2?family=Crimson+Text:wght@400;600;700&display=swap" rel="stylesheet">
<style>
:root{
  --nav-bg:#3a1c2c;
  --nav-bg-2:#56233a;
  --accent:#f0a21a;
  --accent-deep:#e49413;
  --ink-light:#ffffff;
  --ink-soft:#f1e6dc;
  --panel:rgba(30,12,22,.72);
  --pill:rgba(60,20,20,.75);
  --hero-dark:#2b1420;
  --hero-warm:#8a4a1e;
}
*{margin:0;padding:0;box-sizing:border-box}
html,body{width:1200px;height:858px;overflow:hidden;background:var(--hero-dark)}
body{font-family:"Crimson Text",Georgia,serif;color:var(--ink-light);position:relative}
.site-nav{position:absolute;top:0;left:0;width:1200px;height:48px;
  background:linear-gradient(90deg,var(--nav-bg),var(--nav-bg-2) 50%,var(--nav-bg));
  display:flex;align-items:center;justify-content:space-between;padding:0 30px 0 32px;z-index:3;overflow:hidden}
.site-nav a{color:var(--ink-light);text-decoration:none;font-size:18px;padding:0 3px;line-height:48px;white-space:nowrap;flex:none}
.site-nav a.is-current{background:var(--accent);font-weight:700;padding:0 9px}
.hero-photo{position:absolute;top:48px;left:0;width:1200px;height:758px;
  background:
   radial-gradient(ellipse 260px 360px at 440px 380px,#c79880 0%,#7a4a3a 60%,transparent 100%),
   radial-gradient(circle 120px at 900px 220px,rgba(240,170,70,.55),transparent),
   radial-gradient(circle 140px at 1100px 480px,rgba(235,160,60,.45),transparent),
   radial-gradient(circle 100px at 120px 260px,rgba(230,150,60,.4),transparent),
   linear-gradient(180deg,var(--hero-warm),var(--hero-dark) 90%)}
.hero-arc{position:absolute;top:48px;left:0;width:1200px;height:758px;z-index:1}
.contact-tools{position:absolute;top:66px;left:42px;display:flex;align-items:center;gap:10px;z-index:2;font-weight:700;font-size:19px;white-space:nowrap}
.tagline{position:absolute;top:72px;left:682px;font-size:19px;z-index:2;white-space:nowrap}
.badge{position:absolute;top:66px;left:1084px;z-index:2}
.brand{position:absolute;top:258px;left:664px;z-index:2;white-space:nowrap}
.brand .pre{font-size:30px;line-height:1}
.brand .name{font-size:54px;line-height:1.05;letter-spacing:.5px}
.brand .sub{font-size:23px;line-height:1.1}
.call{position:absolute;top:392px;left:668px;z-index:2;background:var(--pill);border-radius:10px;padding:4px 14px;font-size:27px;font-weight:600;white-space:nowrap}
.call span{font-weight:400}
.note{position:absolute;top:436px;left:672px;font-size:18px;z-index:2}
.panel{position:absolute;top:600px;height:180px;background:var(--panel);border-radius:10px;padding:16px 38px;z-index:2}
.panel h2{color:var(--accent);font-size:20px;font-weight:700;margin-bottom:8px}
.panel li{list-style:none;font-size:17px;line-height:21px;color:var(--ink-soft)}
.panel .more{position:absolute;right:36px;bottom:12px;color:var(--accent);font-size:17px;text-decoration:underline}
.panel-resources{left:36px;width:366px}
.panel-articles{left:416px;width:362px}
.panel-updates{left:792px;width:364px}
.site-footer{position:absolute;left:0;top:806px;width:1200px;height:52px;background:var(--accent-deep);
  text-align:center;line-height:52px;font-size:19px;z-index:3}
</style>
</head>
<body>
<nav class="site-nav">
  <a class="is-current" href="#">Home</a><a href="#">Contactme</a><a href="#">Criminal Law</a><a href="#">Family Law</a><a href="#">Will Drafting</a><a href="#">Attorney</a><a href="#">Profile Fees</a><a href="#">Legal Updates</a><a href="#">Online Resources</a><a href="#">Legal updates</a><a href="#">Article</a>
</nav>

<div class="hero-photo" role="img" aria-label="Portrait of the attorney in a white shirt and tie against a warm blurred office background"></div>
<svg class="hero-arc" width="1200" height="758" viewBox="0 0 1200 758">
  <path d="M0 0 H1200 V758 H1130 C1130 300 900 60 560 60 C240 60 60 260 40 758 H0 Z" fill="rgba(45,15,35,.55)"/>
  <path d="M40 758 C60 260 240 60 560 60 C900 60 1130 300 1130 758" fill="none" stroke="rgba(255,220,180,.25)" stroke-width="2"/>
</svg>

<div class="contact-tools">
  <svg width="40" height="34" viewBox="0 0 40 34"><rect x="2" y="4" width="36" height="26" rx="3" fill="#f3efe8"/><path d="M2 6 L20 20 L38 6" fill="none" stroke="#8a6a4a" stroke-width="2"/></svg>
  <svg width="30" height="30" viewBox="0 0 30 30"><circle cx="15" cy="15" r="14" fill="#2f6fd6"/><path d="M10 8 c-2 2 -1 7 4 11 s8 5 9 3 l-2-3 -3 1 c-2-1-4-3-5-5 l1-3 z" fill="#fff"/></svg>
  <span>Voice Line</span>
</div>

<p class="tagline">*Specializing in Criminal Defense and Family Law</p>
<svg class="badge" width="40" height="40" viewBox="0 0 40 40"><circle cx="20" cy="20" r="18" fill="none" stroke="rgba(255,255,255,.55)" stroke-width="2"/></svg>

<div class="brand">
  <p class="pre">Law Offices of</p>
  <p class="name">Morgan Vales, PLLC</p>
  <p class="sub">Affordable Legal Representation</p>
</div>
<p class="call">call us at <span>(612) 555-0148</span></p>
<p class="note">*free consultation</p>

<section class="panel panel-resources">
  <h2>Online Resources</h2>
  <ul>
    <li>Minnesota Rules of Evidence</li>
    <li>Rules of the Court</li>
    <li>Minnesota Rules of Criminal Procedure</li>
    <li>Minnesota Rules of Civil Procedure</li>
  </ul>
  <a class="more" href="#">more ..</a>
</section>
<section class="panel panel-articles">
  <h2>Articles</h2>
  <ul>
    <li>Proportionality and Predictability in Minnesota</li>
    <li>Proportionality and Predictability in Minnesota</li>
  </ul>
  <a class="more" href="#">more ..</a>
</section>
<section class="panel panel-updates">
  <h2>Legal Updates</h2>
  <ul>
    <li>Proportionality and Predictability in Minnesota</li>
    <li>Proportionality and Predictability in Minnesota</li>
  </ul>
  <a class="more" href="#">more ..</a>
</section>

<footer class="site-footer">© 2012 Law Offices of Morgan Vales PLLC</footer>
</body>
</html>
```